Flyer-Design für Pfandhaus
Zielgruppe
Wir vergeben Pfandkrediten für
- Gold und Silberschmuck
- Goldbarren und Münzen
- Technik ( Spielkonsolen , Kameras , Laptop , Smartphones , Tablets )
- Hochwertiges Werkzeug ( Vorlo , Teruno , Grenz Werkpro etc.)
Desweiteren wird Gold angekauft in allen Arten ( Altgold , Bruchgold , Zahngold , Barren , Münzen , Schmuck und Uhren )
Aufgabenstellung
Wichtig sind die Beiden Hauptsachen
Pfandhaus - Goldankauf würde das gerne mit ca. 2 Bilder etwas untermalen.
Sie könne unter meiner Homepage www.leihhaus-mebold.de mein Farbkonzept erkennen bin aber daran nicht fix gebunden wenn es andere Kreative Ideen vorkommen.
Ich möchte die Flyer gerne verteilen lassen als Beilage oder direktverteilung soll also etwas auffallen.

```html
<!DOCTYPE html>
<html lang="de">
<head>
<meta charset="utf-8">
<title>Leihhaus Mebold – Pfandkredit &amp; Goldankauf</title>
<link href="https://fonts.googleapis.com/css2?family=Source+Sans+3:wght@400;600;700;800&display=swap" rel="stylesheet">
<style>
  :root {
    --dark: #4a4849;
    --gold: #ad9763;
    --gold-line: #b3a06c;
    --red: #cc1719;
    --white: #ffffff;
    --paper: #ffffff;
    --note-light: #eeebf3;
    --note-dark: #b3a8cf;
    --jewel-light: #eccb5c;
    --jewel-dark: #c99a26;
  }
  * { margin: 0; padding: 0; box-sizing: border-box; }
  html, body { width: 1200px; height: 848px; overflow: hidden; background: var(--paper); }
  body { font-family: "Source Sans 3", "Myriad Pro", sans-serif; position: relative; color: var(--gold); }
  .panel { position: absolute; top: 0; width: 598px; height: 848px; overflow: hidden; background: var(--paper); }
  .panel--loan { left: 0; }
  .panel--gold { left: 603px; width: 597px; }
  .band { position: absolute; left: 0; right: 0; background: var(--dark); display: flex; align-items: center; justify-content: center; }
  .band--top { top: 0; height: 142px; border-bottom: 3px solid var(--gold-line); }
  .band--bottom { bottom: 0; height: 77px; border-top: 3px solid var(--gold-line); }
  .headline { color: var(--white); font-weight: 700; font-size: 88px; letter-spacing: 1.5px; line-height: 1; padding-top: 6px; text-shadow: 3px 4px 5px rgba(0,0,0,.55); }
  .web { color: var(--white); font-weight: 700; font-size: 45px; line-height: 1; text-shadow: 2px 3px 4px rgba(0,0,0,.5); }
  .abs { position: absolute; line-height: 1.2; white-space: nowrap; }
  .intro-question { left: 26px; top: 163px; font-size: 35px; font-weight: 700; }
  .intro-answer { left: 26px; top: 206px; font-size: 26px; font-weight: 700; }
  .benefits { position: absolute; left: 0; top: 262px; width: 598px; height: 134px;
    background: linear-gradient(90deg, var(--red) 0, var(--red) 428px, rgba(204,23,25,0) 598px); color: var(--white); }
  .benefits__title { position: absolute; left: 25px; top: 14px; font-size: 16.5px; font-weight: 700; }
  .benefits__list { position: absolute; left: 25px; top: 44px; list-style: none; font-size: 17px; line-height: 24.5px; }
  .offer-title { left: 26px; top: 423px; font-size: 28px; font-weight: 700; line-height: 33px; }
  .offer-list { position: absolute; left: 25px; top: 508px; list-style: none; }
  .offer-list__item { position: relative; padding-left: 26px; font-size: 23px; font-weight: 600; line-height: 30px; }
  .offer-list__item::before { content: ""; position: absolute; left: 1px; top: 14px; width: 5px; height: 5px; border-radius: 50%; background: var(--gold); }
  .offer-list__sub { list-style: none; padding-left: 15px; font-size: 15.5px; font-weight: 400; line-height: 19px; margin-bottom: 13px; }
  .offer-list__sub .spaced { margin-top: 3px; }
  .money-visual { position: absolute; left: 328px; top: 400px; }
  .instant-cash { position: absolute; left: 0; top: 163px; width: 254px; height: 112px;
    background: linear-gradient(90deg, var(--red) 0, var(--red) 186px, rgba(204,23,25,0) 254px);
    color: var(--white); font-weight: 700; font-size: 38px; line-height: 46px; text-align: center; padding: 11px 38px 0 0;
    text-shadow: 2px 3px 4px rgba(0,0,0,.5); }
  .gold-word { right: 32px; top: 142px; font-size: 130px; font-weight: 700; line-height: 1.1; letter-spacing: -1px; }
  .goods { position: absolute; right: 22px; text-align: right; font-weight: 700; line-height: 1.2; }
  .goods--schmuck { top: 269px; font-size: 57px; }
  .goods--muenzen { top: 334px; font-size: 49px; }
  .goods--barren { top: 390px; font-size: 41px; }
  .goods--silber { top: 438px; font-size: 30px; }
  .jewellery-visual { position: absolute; left: 16px; top: 290px; }
  .divider { position: absolute; left: 12px; top: 472px; width: 574px; height: 2px; background: var(--gold-line); }
  .branch { position: absolute; font-size: 17px; line-height: 20.5px; font-style: normal; }
  .branch__city { font-weight: 700; font-size: 17px; letter-spacing: .3px; }
  .branch--sb { left: 58px; top: 480px; }
  .branch--trier { left: 326px; top: 480px; }
  .branch--mainz { left: 58px; top: 588px; }
  .branch--wi { left: 326px; top: 588px; }
  .hours { position: absolute; left: 0; width: 597px; text-align: center; }
  .hours__title { top: 711px; font-size: 20px; font-weight: 700; }
  .hours__text { top: 740px; font-size: 15.8px; }
</style>
</head>
<body>
  <section class="panel panel--loan">
    <header class="band band--top"><h1 class="headline">PFANDKREDIT</h1></header>

    <p class="abs intro-question">SIE BENÖTIGEN BARGELD?</p>
    <p class="abs intro-answer">KEIN PROBLEM MIT UNSEREM PFANDKREDIT!</p>

    <div class="benefits">
      <p class="benefits__title">Problemlose Geldbeschaffung für jedermann:</p>
      <ul class="benefits__list">
        <li>Schnell, einfach und unbürokratisch in der Abwicklung</li>
        <li>Ideal zum Überbrücken kurzfristiger finanzieller Engpässe</li>
        <li>Keine Gehaltsnachweise, Finanzauskünfte etc. erforderlich</li>
      </ul>
    </div>

    <svg class="money-visual" width="270" height="372" role="img" aria-label="Fächer aus Euro-Banknoten">
      <defs>
        <linearGradient id="notes" x1="0" y1="0" x2="1" y2="1">
          <stop offset="0" stop-color="var(--note-light)"/>
          <stop offset="1" stop-color="var(--note-dark)"/>
        </linearGradient>
      </defs>
      <rect width="270" height="372" fill="url(#notes)"/>
    </svg>

    <h2 class="abs offer-title">WIR VERGEBEN PFANDKREDITE<br>FÜR:</h2>
    <ul class="offer-list">
      <li class="offer-list__item">Goldbarren und Münzen</li>
      <li class="offer-list__item" style="margin-top:5px">Technik
        <ul class="offer-list__sub">
          <li>Spielkonsolen</li>
          <li>Kameras</li>
          <li>Laptop</li>
          <li>Smartphones</li>
          <li class="spaced">Tablets ect.</li>
        </ul>
      </li>
      <li class="offer-list__item">Hochwertiges Werkzeug
        <ul class="offer-list__sub">
          <li>Vorlo</li>
          <li>Teruno</li>
          <li>Grenz Werkpro etc.</li>
        </ul>
      </li>
    </ul>

    <footer class="band band--bottom"><p class="web">WWW.LEIHHAUS-MEBOLD.DE</p></footer>
  </section>

  <section class="panel panel--gold">
    <header class="band band--top"><h1 class="headline">GOLDANKAUF</h1></header>

    <div class="instant-cash">SOFORT<br>BARGELD!</div>

    <p class="abs gold-word">Gold</p>
    <p class="goods goods--schmuck">Schmuck</p>
    <p class="goods goods--muenzen">Münzen</p>
    <p class="goods goods--barren">Barren</p>
    <p class="goods goods--silber">Silber</p>

    <svg class="jewellery-visual" width="322" height="170" role="img" aria-label="Goldschmuck, Ringe, Münzen und ein Goldbarren">
      <defs>
        <radialGradient id="goldpile" cx=".5" cy=".5" r=".6">
          <stop offset="0" stop-color="var(--jewel-light)"/>
          <stop offset=".7" stop-color="var(--jewel-dark)"/>
          <stop offset="1" stop-color="var(--jewel-dark)" stop-opacity="0"/>
        </radialGradient>
      </defs>
      <rect width="322" height="170" fill="url(#goldpile)"/>
    </svg>

    <div class="divider"></div>

    <address class="branch branch--sb">
      <div class="branch__city">SAARBRÜCKEN</div>
      Lindenhofstraße 4<br>66111 Saarbrücken<br>Tel: 0681 - 41 203 500
    </address>
    <address class="branch branch--trier">
      <div class="branch__city">TRIER</div>
      Kastanienweg 7<br>54290 Trier<br>Tel: 0651 - 30 218 640
    </address>
    <address class="branch branch--mainz">
      <div class="branch__city">MAINZ</div>
      Mühlgasse 21<br>55116 Mainz<br>Tel: 06131 - 512 70 70
    </address>
    <address class="branch branch--wi">
      <div class="branch__city">WIESBADEN</div>
      Ahornstraße 62, Eingang:<br>Lindenallee<br>65185 Wiesbaden<br>Tel: 0611 - 73402816
    </address>

    <p class="abs hours hours__title">ÖFFNUNGSZEITEN:</p>
    <p class="abs hours hours__text">Montag bis Freitag 9:30 bis 18:00 Uhr, Samstag 9:30 bis 14:00 Uhr</p>

    <footer class="band band--bottom"><p class="web">WWW.LEIHHAUS-MEBOLD.DE</p></footer>
  </section>
</body>
</html>
```